Visitenkartenerstellung für Quendal-Estates
Zielgruppe
Männer und Frauen, junge Familien bis hin zum Senior.
Verkauf von hochwertigen Immobilien in Spanien.
Aufgabenstellung
Auf Grund unserer Namensänderung benötigen wir ein neues Visitenkartendesign.
Wir sind eine skandinavische Agentur für Luxus-Immobilien auf Mallorca.
Das Design sollte dementsprechend edel aber dennoch schlicht gestaltet sein!

```html
<!DOCTYPE html>
<html lang="en">
<head>
<meta charset="utf-8">
<title>Quendal-Estates – Business Card</title>
<link rel="stylesheet" href="https://fonts.googleapis.com/css2?family=Lato:wght@300;400;700&display=swap">
<style>
  :root {
    --canvas-bg: #ededee;
    --front-bg: #b5b6b9;
    --back-bg: #ffffff;
    --card-edge: #5a5a5c;
    --ink-dark: #1f1f21;
    --ink-text: #3b3b3d;
  }
  * { margin: 0; padding: 0; box-sizing: border-box; }
  html, body {
    width: 1200px;
    height: 754px;
    overflow: hidden;
    background: var(--canvas-bg);
    font-family: "Lato", Arial, sans-serif;
  }
  .canvas {
    position: relative;
    width: 1200px;
    height: 754px;
  }
  .card {
    position: absolute;
    border: 1px solid var(--card-edge);
  }
  .card--front {
    left: 177px;
    top: 92px;
    width: 485px;
    height: 313px;
    background: var(--front-bg);
  }
  .card--back {
    left: 564px;
    top: 354px;
    width: 483px;
    height: 312px;
    background: var(--back-bg);
  }
  .brand-name {
    position: absolute;
    left: 76px;
    top: 112px;
    font-size: 38px;
    font-weight: 300;
    color: var(--ink-dark);
    letter-spacing: 0.2px;
    white-space: nowrap;
  }
  .brand-tagline {
    position: absolute;
    left: 77px;
    top: 180px;
    font-size: 16px;
    font-weight: 300;
    color: var(--ink-text);
    white-space: nowrap;
  }
  .person {
    position: absolute;
    left: 30px;
    top: 94px;
    color: var(--ink-text);
  }
  .person-name {
    font-size: 20px;
    font-weight: 700;
    color: var(--ink-dark);
    letter-spacing: 0.3px;
    line-height: 24px;
  }
  .person-role {
    font-size: 15.5px;
    font-weight: 300;
    line-height: 20px;
  }
  .address {
    position: absolute;
    left: 297px;
    top: 97px;
    font-style: normal;
    font-size: 16px;
    font-weight: 300;
    line-height: 24.5px;
    color: var(--ink-text);
    white-space: nowrap;
  }
  .web-contact {
    position: absolute;
    left: 29px;
    top: 231px;
    font-size: 16px;
    font-weight: 300;
    line-height: 22px;
    color: var(--ink-text);
    white-space: nowrap;
  }
</style>
</head>
<body>
  <main class="canvas">
    <section class="card card--front" aria-label="Card front">
      <p class="brand-name">Quendal-Estates.com</p>
      <p class="brand-tagline">Luxury Real Estate on Mallorca &amp; Ibiza</p>
    </section>

    <section class="card card--back" aria-label="Card back">
      <div class="person">
        <p class="person-name">INGRID HOLMQVIST</p>
        <p class="person-role">Property Manager</p>
      </div>
      <address class="address">
        C. Pinar 12<br>
        07184 Portals Spain<br>
        Tel. 971480256<br>
        Mobil 0034 61583047
      </address>
      <div class="web-contact">
        <p class="web-email">Ingrid.Holmqvist@quendal-estates.com</p>
        <p class="web-url">www.quendal-estates.se</p>
      </div>
    </section>
  </main>
</body>
</html>
```